HANDYMAN SERVICES

we provide a good,and reliable service.we do all aspects of home improvement ,also all garden services,and any repairs,no job too small,free quotes .
I am aiming towards the general public for clients,also be doing special rates for the elderly,and reducing the price for anyone who does a friend reference. It will be free quotes/consultation,all work will be guaranteed.
Now the type of work we do is cctv installation,decking,patio/driveway cleaning,garages for erecting/repairs,house/garage clearances,fit alarm systems,fit or repair windows/doors,lay patios,repair roofs,decorate interior/external,erect ariaels,lay driveways,erect or repair fencing,lay drainage,repair or erect guttering and soffits,water features,erect or repair kitchens/bathrooms,also plastering,lay lawns or repair,also repair/erect sheds.

```html
<!DOCTYPE html>
<html lang="en">
<head>
<meta charset="utf-8">
<title>Handyman Service Flyer</title>
<link rel="stylesheet" href="https://fonts.googleapis.com/css2?family=Gelasio:wght@700&family=Mulish:wght@400;500&display=swap">
<style>
  :root {
    --page: #ffffff;
    --white: #ffffff;
    --accent: #f5b724;
    --band-top: rgba(72, 78, 165, 0.62);
    --band-bottom: rgba(52, 70, 168, 0.86);
    --photo-silver: #9aa4ae;
    --photo-grey: #6f7784;
    --photo-yellow: #e8b83a;
    --photo-blue: #2f44a6;
    --photo-green: #7fae6a;
  }
  * { margin: 0; padding: 0; box-sizing: border-box; }
  html, body { width: 1200px; height: 1000px; overflow: hidden; background: var(--page); }
  .flyer {
    position: absolute; left: 109px; top: 146px; width: 992px; height: 699px;
    overflow: hidden; color: var(--white);
  }
  .flyer__photo {
    position: absolute; inset: 0;
    background:
      radial-gradient(ellipse 260px 120px at 430px 20px, var(--photo-yellow), transparent 70%),
      radial-gradient(ellipse 180px 200px at 40px 400px, var(--photo-green), transparent 70%),
      linear-gradient(90deg, var(--photo-silver) 0%, var(--photo-grey) 32%, #5a5f86 48%, var(--photo-blue) 72%, #3a4fb0 100%);
  }
  .band-top {
    position: absolute; left: 0; top: 62px; width: 100%; height: 303px;
    background: var(--band-top);
  }
  .band-bottom {
    position: absolute; left: 0; top: 459px; width: 100%; height: 173px;
    background: var(--band-bottom);
  }
  .serif { font-family: "Gelasio", Georgia, serif; font-weight: 700; }
  .contact {
    position: absolute; left: 60px; top: 94px; width: 240px;
    font-size: 27px; line-height: 34px;
  }
  .contact__phone { color: var(--accent); }
  .divider {
    position: absolute; left: 320px; top: 102px; width: 1.5px; height: 222px;
    background: var(--white);
  }
  .offer { position: absolute; left: 353px; top: 92px; width: 620px; }
  .offer__lead { font-size: 26.5px; line-height: 35px; }
  .offer__points {
    list-style: none; margin-top: 16px;
    font-family: "Mulish", Arial, sans-serif; font-size: 20px; line-height: 30px;
  }
  .offer__points li { position: relative; padding-left: 28px; }
  .offer__points li::before {
    content: "•"; position: absolute; left: 4px; color: var(--accent);
  }
  .title {
    position: absolute; left: 313px; top: 368px;
    font-size: 62px; line-height: 80px; white-space: nowrap;
  }
  .title__accent { color: var(--accent); }
  .services {
    position: absolute; left: 0; top: 475px; width: 100%;
    text-align: center; font-family: "Mulish", Arial, sans-serif;
    font-size: 17.5px; line-height: 26.8px;
  }
  .services .dot { color: var(--accent); margin: 0 6px; }
</style>
</head>
<body>
  <main class="flyer">
    <div class="flyer__photo" role="img" aria-label="Photo of a tradesman in blue overalls and yellow hard hat fitting chrome plumbing under a sink"></div>
    <div class="band-top"></div>
    <div class="band-bottom"></div>

    <p class="contact serif">For more information or a free quote please call <span class="contact__phone">07700 900123</span></p>
    <div class="divider"></div>

    <section class="offer">
      <h2 class="offer__lead serif">We provide a good, reliable service that covers all aspects of home improvement, garden services and any repairs.</h2>
      <ul class="offer__points">
        <li>No job is too small</li>
        <li>Special rates for the Senior Citizens and friend referrals</li>
        <li>Free quotes and consultations</li>
        <li>All work is guaranteed</li>
      </ul>
    </section>

    <h1 class="title serif">Handyman <span class="title__accent">Service</span></h1>

    <p class="services">
      CCTV and alarm installation<span class="dot">•</span>Decking<span class="dot">•</span>Patios<span class="dot">•</span>Driveway cleaning<br>
      Fitting or repairing windows and doors<span class="dot">•</span>Garage/shed erecting and repairs<span class="dot">•</span>Roof repairs<br>
      House/garage clearances<span class="dot">•</span>Decorating, interior and external<span class="dot">•</span>Erecting aerials<span class="dot">•</span>Laying driveways<br>
      Fence erection or repair<span class="dot">•</span>Lay drainage, repairing or erecting guttering and soffits<span class="dot">•</span>Water features<br>
      Kitchen and bathroom fitting or repairs<span class="dot">•</span>Plastering<span class="dot">•</span>Lawn laying
    </p>
  </main>
</body>
</html>
```